Business Card Professional Clean - Ledgerpeak

Create a business card for my company that deals with Cryptocurrencies. I have a few designs ideas that I'd like to be implemented. Thanks! I will include the logo files, and a link to the design styles that I like.

Target Market(s)

Professionals

Industry/Entity Type

Consulting

Contact Information for Business Card

Name: Mark Dunn
Title: CEO/Technical Director
Phone: (587)430-9158
E-mail: mdunn@ledgerpeak.example
Address: Suite 512, 208-3375 Harwood Lane NW

Twitter: @LedgerPeakYYC
Instagram: ledgerpeakyyc

Colors
92b5d7
3276b5
33a6d7
85acd3
85cae6
0592cd

Requirements
Must have
• Some colors that match with the logo and the pictures I put in below.
• Ideally the finished product would look something like the attachments showing the color gradient I want.
Nice to have
• Please see some of the attachments I've included. This is very close to the final product that I would like to see. If someone could recreate something like those I would definitely feel pretty good about it.
• For the instagram and twitter please use the symbols/icon to represent it on the card.
Should not have
• No crazy colors and unprofessional styles. I just want clear info. Don't go outside the boundaries of the colors in the attachment and we should be good. No crazy weird fonts either.

```html
<!DOCTYPE html>
<html lang="en">
<head>
<meta charset="utf-8">
<title>Ledgerpeak Business Card</title>
<link rel="stylesheet" href="https://fonts.googleapis.com/css2?family=Marcellus+SC&family=Crimson+Text:wght@400&display=swap">
<style>
  :root {
    --backdrop: #b9b9b9;
    --brand-blue: #0b4f97;
    --brand-blue-deep: #084486;
    --brand-blue-light: #12579f;
    --paper: #f2f2f2;
    --paper-shade: #dcdcdc;
    --edge-shadow: #3b4048;
    --ink-light: #ffffff;
    --ink-soft: #e6ecf4;
  }
  * { box-sizing: border-box; margin: 0; padding: 0; }
  html, body {
    width: 1200px;
    height: 576px;
    overflow: hidden;
    background: var(--backdrop);
  }
  .canvas {
    position: relative;
    width: 1200px;
    height: 576px;
  }
  .card {
    position: absolute;
    top: 138px;
    width: 484px;
    height: 293px;
    border-radius: 13px;
    overflow: hidden;
  }
  .card-front {
    left: 82px;
    background: linear-gradient(160deg, var(--brand-blue-light) 0%, var(--brand-blue) 50%, var(--brand-blue-deep) 100%);
  }
  .front-wordmark {
    position: absolute;
    left: 0;
    right: 0;
    top: 118px;
    text-align: center;
    font-family: "Marcellus SC", serif;
    font-size: 46px;
    letter-spacing: 1px;
    color: var(--ink-soft);
  }
  .card-back {
    left: 602px;
    width: 481px;
    height: 291px;
  }
  .back-shape {
    position: absolute;
    inset: 0;
    width: 481px;
    height: 291px;
  }
  .holder-name {
    position: absolute;
    left: 35px;
    top: 29px;
    font-family: "Marcellus SC", serif;
    font-size: 25px;
    letter-spacing: 1px;
    color: var(--ink-light);
  }
  .holder-title {
    position: absolute;
    left: 35px;
    top: 63px;
    font-family: "Crimson Text", serif;
    font-size: 12.5px;
    color: var(--ink-soft);
  }
  .address {
    position: absolute;
    left: 35px;
    top: 161px;
    font-family: "Crimson Text", serif;
    font-size: 13.5px;
    line-height: 19px;
    color: var(--ink-soft);
  }
  .contact-list {
    position: absolute;
    left: 35px;
    top: 205px;
    list-style: none;
    font-family: "Crimson Text", serif;
    font-size: 13.5px;
    color: var(--ink-soft);
  }
  .contact-item {
    display: flex;
    align-items: center;
    height: 18.5px;
  }
  .contact-icon {
    width: 11px;
    height: 11px;
    margin-right: 15px;
    fill: var(--ink-soft);
  }
  .back-wordmark {
    position: absolute;
    left: 414px;
    top: 145px;
    transform: translate(-50%, -50%) rotate(-90deg);
    white-space: nowrap;
    font-family: "Marcellus SC", serif;
    font-size: 34px;
    letter-spacing: 1px;
    color: var(--brand-blue);
  }
</style>
</head>
<body>
<main class="canvas">

  <section class="card card-front" aria-label="Card front">
    <p class="front-wordmark">Ledgerpeak</p>
  </section>

  <section class="card card-back" aria-label="Card back">
    <svg class="back-shape" viewBox="0 0 481 291" aria-hidden="true">
      <defs>
        <linearGradient id="back-blue" x1="0" y1="0" x2="0.4" y2="1">
          <stop offset="0" stop-color="#12579f"/>
          <stop offset="1" stop-color="#084486"/>
        </linearGradient>
        <linearGradient id="back-paper" x1="0" y1="0" x2="1" y2="1">
          <stop offset="0" stop-color="#f6f6f6"/>
          <stop offset="1" stop-color="#e2e2e2"/>
        </linearGradient>
      </defs>
      <rect class="back-blue-field" width="481" height="291" fill="url(#back-blue)"/>
      <path class="back-curve-edge" d="M300,0 Q226,145 280,291 L481,291 L481,0 Z" fill="#3b4048"/>
      <path class="back-paper-field" d="M300,0 Q237,145 290,291 L481,291 L481,0 Z" fill="url(#back-paper)"/>
    </svg>

    <h1 class="holder-name">Mark Dunn</h1>
    <p class="holder-title">CEO/Technical Director</p>

    <p class="address">Suite 512, 208-3375<br>Harwood Lane NW</p>

    <ul class="contact-list">
      <li class="contact-item">
        <svg class="contact-icon" viewBox="0 0 12 12" aria-hidden="true">
          <path d="M1 3.5 Q6 0.5 11 3.5 L10 5 L8 4.2 L8 3.4 Q6 2.8 4 3.4 L4 4.2 L2 5 Z"/>
          <path d="M3.2 5.2 L8.8 5.2 L10.5 10.5 L1.5 10.5 Z"/>
        </svg>
        <span>(587)430-9158</span>
      </li>
      <li class="contact-item">
        <svg class="contact-icon" viewBox="0 0 12 12" aria-hidden="true">
          <path d="M0.5 2.5 H11.5 V9.5 H0.5 Z M1.5 3.3 L6 6.8 L10.5 3.3" fill="none" stroke="#e6ecf4" stroke-width="1.1"/>
        </svg>
        <span>mdunn@ledgerpeak.example</span>
      </li>
      <li class="contact-item">
        <svg class="contact-icon" viewBox="0 0 12 12" aria-hidden="true">
          <g fill="none" stroke="#e6ecf4" stroke-width="1">
            <circle cx="6" cy="6" r="5"/>
            <ellipse cx="6" cy="6" rx="2.2" ry="5"/>
            <path d="M1 6 H11 M2 3.3 H10 M2 8.7 H10"/>
          </g>
        </svg>
        <span>www.ledgerpeak.example</span>
      </li>
    </ul>

    <p class="back-wordmark">Ledgerpeak</p>
  </section>

</main>
</body>
</html>
```